Web Site Design For Costa Alta Homes Project

The idea behind this project is pretty simple. I am putting my penthouse apartment up for sale and am trying to be creative in selling it.
Technically this will be pretty simple, it will be 3 pages but graphically this has to be as impressive as possible which is why I am trying Pixel Harbor.
The apartment is located in Barra Da Tijuca, Rio De Janeiro, Brazil. (This is where the 2016 Meridian Regatta will be held)
I am looking for an index page and 2 sub-pages. I am open to all kinds of designs and navigation's but it has to make an impression quickly with a professional and enticing design. The index page should make it obvious that there is a penthouse apartment for sale in Barra Da Tijuca ( suburb of Rio De Janeiro). The first sub page is about the Condominium where the apartment is located, the second sub page is about the apartment itself.
Here is a more detailed description of what the 3 pages should be about.
Index Page
This is the landing page and should make it obvious that there is an apartment for sale in Barra Da Tijuca, Rio De Janeiro with the following attributes
251 SQ M
Duplex Penthouse
4 suites
Price R$ 2.200.000
Price per SQ M: R$ 8.764
First Sub-Page
This is about the Condominium which is called "Gentle Palm Residences" with the following bullets
*Family friendly and safe
*Direct access to the beach
*Many amenities like pool, football court, gym, sauna
There should be some photos of the condominium and a link to the site of the condominium ( www.gprvx.com )
Second Sub-page
This is about the apartment. It should list in bullets the features of the apartment and then have a photo gallery of the view and various rooms. I have attached sample photos but will eventually have to use more photos.
Apartment Features
Price: R$ 2.220.000
251 m2 Duplex Penthouse
4 suites
maids room with bath
guest bathroom
living room
dinning room
Terrace with heated pool for year round use
Veranda
As mentioned above I am open to all designs and navigation so feel free to be creative. The important thing is catch peoples attention and get the message across in a few seconds, which is that there is an apartment for sale at this price with these features in this location. I will then use brightlist promoter and SEO to get people to the site.
Thanks
Target Market(s)
Men and Women from 30-60 years of age.
Industry/Entity Type
Apartment

```html
<!DOCTYPE html>
<html lang="en">
<head>
<meta charset="utf-8">
<title>Costa Alta Homes – Penthouse in Barra Da Tijuca</title>
<link href="https://fonts.googleapis.com/css2?family=Open+Sans:wght@400;600;700&family=PT+Sans+Narrow:wght@400;700&display=swap" rel="stylesheet">
<style>
:root{
  --green:#8db21e;
  --green-dark:#6f8f12;
  --header:#2f2f2f;
  --band:#e4e4e4;
  --red:#c5262c;
  --ink:#3b3b3b;
  --muted:#777;
  --footer:#dcdcdc;
  --footer-dark:#c9c9c9;
  --white:#fff;
  --price:#e9c21a;
}
*{box-sizing:border-box;margin:0;padding:0}
html,body{width:843px;height:1200px;overflow:hidden}
body{background:var(--white);font-family:"Open Sans",Arial,sans-serif;color:var(--ink);font-size:8px;position:relative}
.wrap{position:absolute;left:112px;width:400px}

/* header */
.site-header{position:absolute;top:0;left:0;width:843px;height:58px;background:linear-gradient(#3c3c3c,#262626)}
.brand{position:absolute;left:126px;top:12px;display:flex;align-items:center;gap:8px}
.brand-mark{width:14px;height:14px;background:var(--green)}
.brand-name{font-family:"PT Sans Narrow",sans-serif;font-weight:700;font-size:21px;line-height:22px;color:var(--white)}
.brand-tag{position:absolute;left:126px;top:38px;font-size:6.5px;color:#bbb}
.main-nav{position:absolute;right:98px;top:12px;display:flex}
.main-nav a{color:#ddd;text-decoration:none;font-size:8.5px;padding:5px 9px}
.main-nav a.active{background:var(--green);color:var(--white)}

/* hero */
.hero{position:absolute;top:58px;left:0;width:843px;height:222px;background:linear-gradient(170deg,#8fa9b8 0%,#4d7d98 30%,#2f6a83 48%,#8f9c86 62%,#5b6f46 100%)}
.hero-card{position:absolute;left:547px;top:22px;width:190px;height:178px;background:rgba(20,20,20,.72);padding:10px 12px;color:var(--white)}
.hero-card h1{font-family:"PT Sans Narrow",sans-serif;font-weight:400;font-size:22px;line-height:24px}
.hero-card .price{font-family:"PT Sans Narrow",sans-serif;font-size:16px;color:var(--price);line-height:18px}
.hero-card .facts{color:var(--price);font-size:8px;line-height:11px;margin-top:5px}
.hero-card p{font-size:6.5px;line-height:9px;color:#ccc;margin-top:5px}
.btn{display:inline-block;background:var(--green);color:var(--white);font-size:6.5px;font-weight:700;padding:4px 9px;text-decoration:none}
.hero-card .btn{margin-top:7px;background:#444}
.dots{position:absolute;top:262px;left:463px;display:flex;gap:5px}
.dots span{width:8px;height:8px;border-radius:50%;background:var(--green)}
.dots span.off{background:#ccc}

/* carousel */
.showcase{position:absolute;top:280px;left:0;width:843px;height:195px;background:linear-gradient(var(--white),var(--band) 40%)}
.tiles{position:absolute;left:140px;top:108px;display:flex;gap:14px}
.tile{position:relative;width:142px;height:76px;border:3px solid var(--white);box-shadow:0 1px 3px rgba(0,0,0,.3);overflow:hidden}
.tile .ribbon{position:absolute;right:-20px;top:8px;width:70px;height:12px;background:var(--red);transform:rotate(35deg)}
.tile span{position:absolute;left:8px;bottom:6px;color:var(--white);font-family:"PT Sans Narrow",sans-serif;font-size:13px}
.arrow{position:absolute;top:140px}

/* main */
h2{font-family:"PT Sans Narrow",sans-serif;font-weight:400;font-size:15px;color:var(--ink);padding-bottom:5px;border-bottom:1px solid #ddd;margin-bottom:9px}
.welcome{top:517px}
.welcome .photo{float:left;width:118px;height:80px;margin:0 10px 6px 0;background:linear-gradient(#9fc0d6,#5e8fa8 55%,#8b8f78)}
.welcome p{font-size:7px;line-height:10.5px;color:var(--muted);margin-bottom:7px}
.services{top:762px}
.services .cols{display:flex;gap:30px}
.services ul{list-style:none}
.services li{font-size:7px;color:var(--muted);line-height:12px;padding-left:9px;position:relative}
.services li::before{content:"";position:absolute;left:0;top:4px;width:4px;height:4px;background:var(--red)}
.picks{top:870px}
.picks .cards{display:flex;gap:14px}
.card{width:122px;text-align:center}
.card .photo{height:76px;position:relative}
.card .photo span{position:absolute;left:0;bottom:0;background:rgba(0,0,0,.6);color:var(--white);font-size:6.5px;padding:2px 6px}
.card .cost{font-family:"PT Sans Narrow",sans-serif;font-size:15px;color:var(--red);margin-top:4px}

/* booking */
.booking{position:absolute;left:533px;top:517px;width:212px;height:520px;background:var(--green);padding:10px;color:var(--white)}
.booking h3{font-family:"PT Sans Narrow",sans-serif;font-weight:400;font-size:14px;margin-bottom:6px}
.booking .intro{font-size:6.5px;line-height:9px;margin-bottom:6px}
.field label{display:block;font-size:6.5px;margin:5px 0 2px}
.field .input{height:13px;background:var(--white)}
.field .pair{display:flex;gap:6px}
.field .pair .input{flex:1}
.booking .area{height:40px;background:var(--white)}
.booking .btn{float:right;margin-top:8px;background:var(--green-dark);border:1px solid var(--white)}

/* footer */
.site-footer{position:absolute;top:1060px;left:0;width:843px;height:140px;background:var(--footer)}
.foot-cols{position:absolute;left:122px;top:20px;display:flex;gap:38px}
.foot-cols h4{font-size:7px;font-weight:600;margin-bottom:5px;color:var(--ink)}
.foot-cols ul{list-style:none}
.foot-cols li{font-size:6.5px;color:var(--muted);line-height:10px;padding-left:7px;position:relative}
.foot-cols li::before{content:"";position:absolute;left:0;top:4px;width:3px;height:3px;border-radius:50%;background:var(--muted)}
.social{display:flex;gap:3px}
.social span{width:10px;height:10px;background:#6b6b6b}
.copyright{position:absolute;bottom:0;left:0;width:843px;height:24px;background:var(--footer-dark);text-align:center;line-height:24px;font-size:6.5px;color:var(--muted)}
</style>
</head>
<body>

<header class="site-header">
  <div class="brand">
    <span class="brand-mark"></span>
    <span class="brand-name">Costa Alta Homes</span>
  </div>
  <div class="brand-tag">Lorem ipsum dolor sit amet, consectetur adipiscing elit</div>
  <nav class="main-nav">
    <a class="active" href="#">Home</a><a href="#">About Us</a><a href="#">Buying</a><a href="#">Renting</a><a href="#">Services</a><a href="#">Gallery</a><a href="#">Contact Us</a>
  </nav>
</header>

<section class="hero" role="img" aria-label="Aerial photo of the Barra Da Tijuca beachfront with ocean, towers and hills">
  <div class="hero-card">
    <h1>Barra Da Tijuca</h1>
    <div class="price">Price R$ 2.200.000</div>
    <div class="facts">251 SQ M<br>Duplex Penthouse<br>4 Suites<br>Price per SQ M: R$ 8.764</div>
    <p>Lorem ipsum dolor sit amet, consectetur adipiscing elit. Integer fermentum tempus nibh, sed dictum purus dapibus vitae.</p>
    <a class="btn" href="#">READ MORE</a>
  </div>
</section>
<div class="dots"><span></span><span></span><span></span><span class="off"></span></div>

<section class="showcase">
  <svg class="arrow" style="left:100px" width="10" height="16" viewBox="0 0 10 16"><path d="M9 1 2 8l7 7" fill="none" stroke="#8db21e" stroke-width="3"/></svg>
  <div class="tiles">
    <div class="tile" role="img" aria-label="Photo of ocean view suites" style="background:linear-gradient(#a7c3d4,#4f7f99)"><div class="ribbon"></div><span>Ocean Suites</span></div>
    <div class="tile" role="img" aria-label="Photo of the pool house" style="background:linear-gradient(#d8c7a8,#7a6a55)"><div class="ribbon"></div><span>Pool House</span></div>
    <div class="tile" role="img" aria-label="Photo of the terrace" style="background:linear-gradient(#bfb39b,#5d5448)"><div class="ribbon"></div><span>Terrace</span></div>
    <div class="tile" role="img" aria-label="Photo of ocean view suites at dusk" style="background:linear-gradient(#9ab0c0,#6d6d70)"><div class="ribbon"></div><span>Ocean Suites</span></div>
  </div>
  <svg class="arrow" style="left:760px" width="10" height="16" viewBox="0 0 10 16"><path d="M1 1l7 7-7 7" fill="none" stroke="#8db21e" stroke-width="3"/></svg>
</section>

<main>
  <section class="wrap welcome">
    <h2>Welcome to Our Website</h2>
    <div class="photo" role="img" aria-label="Photo of the beachfront condominium towers"></div>
    <p>Lorem ipsum dolor sit amet, consectetur adipiscing elit. Vestibulum dignissim eros non urna ultrices, at tempor purus aliquet. Nullam vitae lectus vel sem mattis volutpat. Quisque lacinia nunc a augue porta, sed pulvinar mi dictum. Morbi tristique neque eu risus tempor.</p>
    <p>Praesent sed tellus quis ligula viverra feugiat. Suspendisse potenti. Curabitur blandit, nisl at luctus aliquet, arcu sem gravida justo, vitae viverra lorem turpis in nunc. Aenean euismod nulla id magna faucibus, non consequat dui lobortis.</p>
    <p>Donec vel dui a neque aliquam cursus. Etiam ut diam eu odio pharetra varius. Ut vehicula sem vel orci fringilla, sed tempus nisi imperdiet. Integer vel purus sed elit sagittis tincidunt.</p>
    <a class="btn" href="#">READ MORE</a>
  </section>

  <section class="wrap services">
    <h2>Our Services</h2>
    <div class="cols">
      <ul><li>Lorem ipsum dolor sit</li><li>Integer fermentum</li><li>Nullam dapibus vitae</li><li>Donec vel aliquam</li></ul>
      <ul><li>Integer fermentum</li><li>Lorem ipsum dolor</li><li>Quisque lacinia</li><li>Etiam ut pharetra</li></ul>
      <ul><li>Lorem ipsum dolor</li><li>Integer fermentum</li><li>Morbi tristique</li><li>Aenean euismod</li></ul>
    </div>
  </section>

  <section class="wrap picks">
    <h2>We Recommended</h2>
    <div class="cards">
      <div class="card"><div class="photo" role="img" aria-label="Photo of a beachfront apartment tower" style="background:linear-gradient(#b7cfdf,#56819a)"><span>Barra Da Tijuca</span></div><div class="cost">$7899.99</div></div>
      <div class="card"><div class="photo" role="img" aria-label="Photo of a penthouse living room" style="background:linear-gradient(#e2d6c0,#8d7a60)"><span>Penthouse</span></div><div class="cost">$9799.99</div></div>
      <div class="card"><div class="photo" role="img" aria-label="Aerial photo of the coastline towers" style="background:linear-gradient(#9ec1d8,#3d6d8a 60%,#c8c0a8)"><span>Ocean View</span></div><div class="cost">$8699.99</div></div>
    </div>
  </section>

  <aside class="booking">
    <h3>Customized Booking</h3>
    <p class="intro">Fill the enquiry form to make a good customized itinerary. We will reply as soon as possible.</p>
    <div class="field"><label>Full Name</label><div class="input"></div></div>
    <div class="field"><label>Address</label><div class="input"></div></div>
    <div class="field"><label>Contact No</label><div class="input"></div></div>
    <div class="field"><label>Email Id</label><div class="input"></div></div>
    <div class="field"><label>Date of Booking</label><div class="input"></div></div>
    <div class="field"><label>No of Occupants</label><div class="pair"><div class="input"></div><div class="input"></div></div></div>
    <div class="field"><label>Budget per person</label><div class="input"></div></div>
    <div class="field"><label>Place of interest</label><div class="input"></div></div>
    <div class="field"><label>Comments</label><div class="area"></div></div>
    <a class="btn" href="#">Submit</a>
  </aside>
</main>

<footer class="site-footer">
  <div class="foot-cols">
    <div><h4>Lorem ipsum dolor</h4><ul><li>Dolor sit amet</li><li>Integer nibh</li><li>Quisque lacinia</li><li>Etiam pharetra</li><li>Morbi neque</li></ul></div>
    <div><h4>Lorem ipsum dolor sit</h4><ul><li>Dolor sit amet</li><li>Integer nibh</li><li>Quisque lacinia</li></ul></div>
    <div><h4>Lorem ipsum dolor</h4><ul><li>Dolor sit amet</li><li>Integer nibh</li><li>Quisque lacinia</li><li>Etiam pharetra</li></ul></div>
    <div><h4>Lorem ipsum dolor sit</h4><ul><li>Dolor sit amet</li><li>Integer nibh</li><li>Quisque lacinia</li><li>Etiam pharetra</li></ul></div>
    <div><h4>Find Us</h4><div class="social"><span></span><span></span><span></span><span></span></div></div>
  </div>
  <div class="copyright">Copyright Costa Alta Homes 2013, All Rights Reserved</div>
</footer>

</body>
</html>
```